Buch-Cover für „Umbruch. ZACK!“ - Führung in der Gewitterwirtschaft
Liebe Designer,
wir hätten gerne eure Vorschläge für ein neues Management-Buch, das Potential zum Bestseller hat. Wir wollen „Kontinents rasantester Führungsratgeber“ realisieren und haben mit „Vulkan“ ein grafisch spannendes Thema dabei. Es darf und soll auf dem Cover also krachen ohne aufdringlich oder billig zu wirken. Wir freuen uns auf eure Vorschläge und geben regelmäßig Feedback!
Zielgruppe:
Vor allem Manager, aber auch Berater, Agenturmitarbeiter, Journalisten und Studenten (Männer & Frauen zwischen 25 und 65).
Alle, die NEIN zum Status-Quo sagen! Alle, die Wandel als CHANCE sehen! Alle, die ihr Business ZUKUNFTSFIT machen möchten! Alle PIONIERE, Business-Helden und solche, die es werden wollen!
Beste Grüße
Tobias und Konrad
Aufgabenstellung
Buchcovergröße:
34 cm breit komplett, davon ca. 1,5 cm Buchrücken
23 cm hoch
Farben & Schrift:
Wir möchten auffallen. Alles was hohen Kontrast bringt ist gut. Vielleicht ein schwarzes Cover und durch die Schrift scheint dann ein explodierendes Vulkan-Bild hindurch. Das ist aber nur eine erste vage Idee. Front-, Rückseite und Buchdeckel sollen die gleiche Farbe haben. Es darf nicht bedrohlich wirken!
Cover vorne:
Als Autor soll vorne aufs Cover: „Konrad Pellwitz“
Titel: „Umbruch. ZACK!“
Untertitel: „Führung in der Gewitterwirtschaft“
Der Claim kann als separates Element (z.B. als Bubble) aufgenommen werden: „Kontinents rasantester Führungsratgeber“
Das Logo des Quellberg-Verlags ist angehängt und soll unten-mittig auf die Frontseite des Covers.
Das „A“ im Titel ZACK! soll eine Wort-Bild-Marke in Form eines Vulkans werden. Also statt einem richtigen A, ein Vulkan, der das A ersetzt. Das A kann unten z.B. ein Lavabecken haben, oben abgebröckelt sein etc. Wichtig ist, dass wir dieses A mit verschiedenen Lavaständen füllen können; also Lava ist unten im Becken, steigt dann an und explodiert. Es darf nicht zu verspielt-detailliert werden, da es auch in klein erkennbar sein soll und z.B. als Logo auf Socken (Merchandising) funktionieren muss. Der Titel „Umbruch. ZACK!“ könnte so ähnlich werden wie die Logos von Ferrowind-Kinofilmen, z.B. LUNAR.
Auf den Buchrücken soll:
Verlagslogo + Titel
Auf die Rückseite des Buchdeckels soll folgender Text:
„Die DISRUPTIONS-WELLE rollt! Die neue Ökonomie ist wie ein Vulkan, der ständig eruptiert: Geschäftsmodelle, Wertschöpfungsketten, Kundenbedürfnisse – gefühlt ändert sich alles. Laufend schießen neue Spielregeln und Player hervor, die den Status quo ändern und etablierte Unternehmen ANGREIFEN.
Erfahren Sie, wie Sie SICH und IHR UNTERN..

```html
<!DOCTYPE html>
<html lang="de">
<head>
<meta charset="utf-8">
<title>Umbruch. ZACK! – Buchcover</title>
<link rel="stylesheet" href="https://fonts.googleapis.com/css2?family=Anton&family=Barlow:wght@500;600&display=swap">
<style>
  :root {
    --page: #ffffff;
    --night: #1a0706;
    --ember: #5e0f0a;
    --lava: #d8240f;
    --glow: #ff7a1a;
    --spark: #ffd23a;
    --ink: #ffffff;
    --badge: #000000;
  }
  html, body {
    margin: 0;
    padding: 0;
    width: 857px;
    height: 1200px;
    overflow: hidden;
    background: var(--page);
  }
  .book {
    position: absolute;
    left: 70px;
    top: 50px;
    width: 712px;
    height: 1100px;
    display: flex;
    box-shadow: 0 10px 24px rgba(0,0,0,0.18);
    color: var(--ink);
    font-family: "Barlow", "Helvetica Neue", Arial, sans-serif;
  }
  .spine {
    position: relative;
    width: 52px;
    height: 100%;
    overflow: hidden;
    border-right: 1px solid rgba(0,0,0,0.45);
  }
  .spine__photo {
    position: absolute;
    inset: 0;
    background:
      radial-gradient(ellipse 140% 14% at 50% 72%, rgba(255,120,30,0.85) 0%, rgba(216,36,15,0.5) 50%, rgba(0,0,0,0) 100%),
      radial-gradient(ellipse 140% 20% at 50% 35%, rgba(190,30,15,0.6) 0%, rgba(0,0,0,0) 100%),
      linear-gradient(180deg, var(--night) 0%, #3a0906 50%, #2a0705 80%, var(--night) 100%);
  }
  .spine__title,
  .spine__publisher {
    position: absolute;
    left: 0;
    width: 100%;
    display: flex;
    justify-content: center;
    writing-mode: vertical-rl;
    transform: rotate(180deg);
    white-space: nowrap;
  }
  .spine__title {
    top: 40px;
    height: 460px;
    justify-content: flex-start;
    font-weight: 500;
    font-size: 30px;
    letter-spacing: 1px;
  }
  .spine__publisher {
    bottom: 40px;
    height: 190px;
    justify-content: flex-start;
    font-weight: 500;
    font-size: 26px;
    letter-spacing: 2px;
    text-transform: uppercase;
  }
  .cover {
    position: relative;
    width: 660px;
    height: 100%;
    overflow: hidden;
  }
  .cover__photo {
    position: absolute;
    inset: 0;
    background:
      radial-gradient(ellipse 22% 14% at 28% 60%, var(--spark) 0%, rgba(255,160,40,0.7) 35%, rgba(255,80,20,0) 100%),
      radial-gradient(ellipse 55% 30% at 30% 62%, rgba(255,90,20,0.85) 0%, rgba(216,36,15,0.55) 45%, rgba(216,36,15,0) 100%),
      radial-gradient(ellipse 60% 25% at 45% 85%, rgba(216,36,15,0.75) 0%, rgba(120,20,10,0.4) 50%, rgba(0,0,0,0) 100%),
      radial-gradient(ellipse 70% 40% at 40% 30%, rgba(200,30,15,0.7) 0%, rgba(94,15,10,0.4) 55%, rgba(0,0,0,0) 100%),
      linear-gradient(180deg, var(--night) 0%, var(--ember) 45%, #3a0906 75%, var(--night) 100%);
  }
  .cover__author {
    position: absolute;
    top: 72px;
    left: 0;
    width: 100%;
    text-align: center;
    font-weight: 500;
    font-size: 27px;
    letter-spacing: 1px;
  }
  .cover__title {
    position: absolute;
    top: 120px;
    left: 0;
    width: 100%;
    text-align: center;
    margin: 0;
    font-weight: 500;
  }
  .cover__title-lead {
    display: block;
    font-weight: 500;
    font-size: 78px;
    line-height: 1;
    letter-spacing: 2px;
  }
  .cover__title-bang {
    display: block;
    margin-top: 12px;
    font-family: "Anton", "Impact", sans-serif;
    font-weight: 400;
    font-size: 290px;
    line-height: 0.95;
    letter-spacing: 4px;
  }
  .cover__subtitle {
    position: absolute;
    top: 524px;
    left: 0;
    width: 100%;
    text-align: center;
    font-weight: 500;
    font-size: 31px;
    letter-spacing: 0.5px;
    text-transform: uppercase;
  }
  .cover__badge {
    position: absolute;
    left: 392px;
    top: 622px;
    width: 236px;
    height: 236px;
    border-radius: 50%;
    background: var(--badge);
    display: flex;
    align-items: center;
    justify-content: center;
    text-align: center;
    font-weight: 600;
    font-size: 22px;
    line-height: 1.35;
    text-transform: uppercase;
  }
  .cover__publisher {
    position: absolute;
    top: 975px;
    left: 0;
    width: 100%;
    text-align: center;
    font-weight: 500;
    font-size: 56px;
    letter-spacing: 3px;
    text-transform: uppercase;
  }
</style>
</head>
<body>
  <div class="book">
    <aside class="spine">
      <div class="spine__photo" role="img" aria-label="Fortsetzung des Vulkanfotos mit glühender Lava"></div>
      <div class="spine__title">Umbruch. ZACK!</div>
      <div class="spine__publisher">Quellberg</div>
    </aside>
    <article class="cover">
      <div class="cover__photo" role="img" aria-label="Nachtfoto eines ausbrechenden Vulkans mit glühenden Lavaströmen und Funkenregen"></div>
      <div class="cover__author">KONRAD PELLWITZ</div>
      <h1 class="cover__title">
        <span class="cover__title-lead">UMBRUCH.</span>
        <span class="cover__title-bang">ZACK!</span>
      </h1>
      <div class="cover__subtitle">Führung in der Gewitterwirtschaft</div>
      <div class="cover__badge">Kontinents<br>rasantester<br>Führungs-<br>ratgeber</div>
      <div class="cover__publisher">Quellberg</div>
    </article>
  </div>
</body>
</html>
```